New Chirpwall Design Project for a 13.3kW solar system Installed by Talven Energy

We require new artwork for our Chirpwall advertisement of a 13.3kW solar system. Including Morvex 475W N-Type panels and 10kW 1 Phase Pellion inverter. Prices starting from $4799. No sub-contractors. Over 200 + 5 star zentrip reviews. The design is to very clean and not busy. Price and system size is what our customers want. We have always found that the busy designs while conveying a lot of information do not motivate our customers. simple professional designs do however work.

Target Market(s)

homeowners

Industry/Entity Type

solar

Colors
0054AA
0677BA
7BADD7
CADEEF
E8F1F8
EB3D1F
EC4F4E
F09395
F8D3D4
FCEDEE

Requirements
Must have
• must be clean and unbusy design. system size and price is what motivates our customers
Nice to have
• clean pictures of the Morvex 475W N-Type panel and Pellion 10kW 1 Phase inverter.
Should not have
• should not be a busy design with too many words

```html
<!DOCTYPE html>
<html lang="en">
<head>
<meta charset="utf-8">
<title>Talven Energy – 13.3kW Solar System</title>
<link rel="stylesheet" href="https://fonts.googleapis.com/css2?family=Montserrat:wght@500;700;800;900&family=Oswald:wght@300;600;700&display=swap">
<style>
  :root {
    --page-bg: #283868;
    --ad-light: #f1f1f2;
    --ad-dark: #2e3548;
    --brand-red: #c21d2e;
    --white: #ffffff;
    --panel-tone: #1c2233;
    --inverter-tone: #d6d8dc;
    --pill-dark: #25262b;
    --badge-gold: #f5b400;
    --badge-orange: #f08a00;
    --star: #f6b81a;
  }
  html, body {
    margin: 0;
    padding: 0;
    width: 874px;
    height: 1200px;
    overflow: hidden;
    background: var(--page-bg);
  }
  .ad {
    position: absolute;
    top: 163px;
    left: 0;
    width: 874px;
    height: 874px;
    display: block;
  }
  .font-display { font-family: "Montserrat", sans-serif; }
  .font-condensed { font-family: "Oswald", sans-serif; }
  .system-size { font-weight: 800; font-size: 75px; fill: var(--white); letter-spacing: -1px; }
  .system-name { font-weight: 900; font-size: 64px; fill: var(--brand-red); }
  .price-label { font-weight: 300; font-size: 50px; fill: var(--white); }
  .price { font-weight: 700; font-size: 92px; fill: var(--brand-red); }
  .price-note { font-weight: 300; font-size: 40px; fill: var(--white); }
  .rating-value { font-weight: 700; font-size: 42px; fill: var(--ad-dark); }
  .rating-label { font-weight: 500; font-size: 14px; fill: var(--ad-dark); letter-spacing: 1px; }
  .reviews-count { font-weight: 600; font-size: 52px; fill: var(--ad-dark); }
  .reviews-line { font-weight: 700; font-size: 33px; }
  .reviews-strong { fill: var(--ad-dark); font-weight: 900; }
  .reviews-source { fill: var(--brand-red); }
  .brand-name { font-weight: 700; font-size: 34px; fill: var(--ad-dark); }
</style>
</head>
<body>
<svg class="ad" viewBox="0 0 1056 1056" xmlns="http://www.w3.org/2000/svg" aria-label="Talven Energy 13.3kW solar system advertisement">
  <defs>
    <radialGradient id="bg-glow" cx="0.7" cy="0.8" r="0.8">
      <stop offset="0" stop-color="#fafafa"/>
      <stop offset="1" stop-color="#ececed"/>
    </radialGradient>
    <radialGradient id="badge-fill" cx="0.4" cy="0.35" r="0.7">
      <stop offset="0" stop-color="var(--badge-gold)"/>
      <stop offset="1" stop-color="var(--badge-orange)"/>
    </radialGradient>
    <linearGradient id="panel-fill" x1="0" y1="0" x2="1" y2="1">
      <stop offset="0" stop-color="#2a3352"/>
      <stop offset="1" stop-color="var(--panel-tone)"/>
    </linearGradient>
    <linearGradient id="inverter-fill" x1="0" y1="0" x2="1" y2="1">
      <stop offset="0" stop-color="#eceef1"/>
      <stop offset="1" stop-color="var(--inverter-tone)"/>
    </linearGradient>
    <polygon id="star" points="0,-20 5.9,-6.5 20,-6.2 9.2,3 13,17 0,9 -13,17 -9.2,3 -20,-6.2 -5.9,-6.5"/>
  </defs>

  <!-- background -->
  <rect class="ad-background" width="1056" height="1056" fill="url(#bg-glow)"/>
  <path class="dark-sweep" d="M0 0 H722 C800 150 830 450 660 640 C500 800 260 860 0 848 Z" fill="var(--ad-dark)"/>
  <path class="accent-line-top" d="M757 0 C780 45 797 90 804 125" fill="none" stroke="var(--brand-red)" stroke-width="6"/>
  <path class="accent-line-bottom" d="M0 703 C160 790 420 800 610 670" fill="none" stroke="var(--brand-red)" stroke-width="6"/>

  <!-- product imagery -->
  <g class="product-panels" role="img" aria-label="Morvex 475W N-Type solar panels, two panels standing side by side">
    <polygon points="86,74 481,112 481,694 86,640" fill="url(#panel-fill)"/>
  </g>
  <g class="product-inverter" role="img" aria-label="Pellion 10kW single phase solar inverter, silver unit">
    <rect x="61" y="579" width="220" height="240" rx="6" fill="url(#inverter-fill)"/>
  </g>

  <!-- headline circle -->
  <circle class="offer-ring" cx="804" cy="434" r="316" fill="var(--brand-red)"/>
  <circle cx="804" cy="434" r="298" fill="var(--white)"/>
  <circle class="offer-disc" cx="804" cy="434" r="280" fill="var(--ad-dark)"/>
  <g class="offer-dots" fill="var(--brand-red)">
    <circle cx="755" cy="228" r="3.5"/><circle cx="773" cy="228" r="3.5"/><circle cx="791" cy="228" r="3.5"/><circle cx="809" cy="228" r="3.5"/><circle cx="827" cy="228" r="3.5"/>
  </g>
  <text class="font-display system-size" x="796" y="310" text-anchor="middle">13.3kW</text>
  <text class="font-display system-name" x="796" y="380" text-anchor="middle">Solar System</text>
  <line x1="697" y1="419" x2="897" y2="419" stroke="var(--white)" stroke-width="3"/>
  <text class="font-condensed price-label" x="797" y="485" text-anchor="middle">Prices Starting From</text>
  <text class="font-condensed price" x="797" y="582" text-anchor="middle">$4799</text>
  <text class="font-condensed price-note" x="797" y="637" text-anchor="middle">No sub-contractors.</text>

  <!-- rating -->
  <g class="rating-badge">
    <rect x="646" y="784" width="335" height="80" rx="40" fill="var(--pill-dark)"/>
    <circle cx="646" cy="824" r="61" fill="url(#badge-fill)"/>
    <text class="font-display rating-value" x="648" y="834" text-anchor="middle">5.0</text>
    <text class="font-display rating-label" x="648" y="856" text-anchor="middle">RATING</text>
    <g fill="var(--star)">
      <use href="#star" x="738" y="826"/>
      <use href="#star" x="788" y="826"/>
      <use href="#star" x="840" y="826"/>
      <use href="#star" x="891" y="826"/>
      <use href="#star" x="941" y="826"/>
    </g>
  </g>
  <text class="font-condensed reviews-count" x="591" y="957">Over 200 +</text>
  <text class="font-display reviews-line" x="591" y="997"><tspan class="reviews-strong">5 Star </tspan><tspan class="reviews-source">zentrip Reviews</tspan></text>

  <!-- brand -->
  <g class="brand">
    <circle cx="106" cy="950" r="16" fill="var(--brand-red)"/>
    <text class="font-display brand-name" x="134" y="962">Talven Energy</text>
  </g>
</svg>
</body>
</html>
```